Label Design for 2x Chutney Products

We need a label design for 2x Chutney Products.
Zintara Chutney - Red Chili
Zintara Chutney - Green Chili & Coriander
See attached pictures. This is just sample pictures so you get an impression of the product and the colors. Both labels to have as title the generic name "Zintara Chutney" and then added either Red Chili or Green Chili & Coriander. The different terms needs to be good readable and can differ in font/color/size, or in the same style if this makes more sense from design point (as I am not a designer). The labels later on need to be editable in the way that the ingredient list, nutrition list, basis company and production information can be added. If this needs to be done directly and cannot be edited later on please let know. Editable design related the additional text also would be good as the additional information need to be added in different languages (Dutch. German and perhaps French). No clue how this is to be implemented but looking forward to receive some input/solutions on this.
I already had a project to create the company logo. I consider this logo to be used as the product logo and not the company logo. A different company logo later on can be designed from new. This logo is here attached. Either to work with this logo and use it as product logo (perhaps revise the colors) and add the product description or create a new logo for the product from scratch if you feel too. The logo itself should be easily readable for the product name/description and the colors appealing to such product and of course customers.
Please contact if any clarification needed. Thanks in advance for your efforts and ideas for this project.

Industry/Entity Type

Food

Other font styles liked:
• Asian Touch

Requirements
Nice to have
• If possible "simply" editable for text fields in order to add/revise the ingredient list, nutrition list, revise to different languages.

```html
<!DOCTYPE html>
<html lang="en">
<head>
<meta charset="utf-8">
<title>Zintara Chutney – Label Set</title>
<link rel="stylesheet" href="https://fonts.googleapis.com/css2?family=Quicksand:wght@600;700&family=Source+Sans+3:wght@300;400;600&display=swap">
<style>
  :root {
    --page-bg: #ffffff;
    --ink: #3a3a3a;
    --ink-soft: #4a4a4a;
    --ink-body: #505050;
    --red: #e3131b;
    --red-deep: #b3151a;
    --green: #35a845;
    --green-deep: #1f7a33;
    --label-red-bg: #e6e6e8;
    --label-green-bg: #dcefe3;
    --name-ink: #2a1010;
  }
  * { box-sizing: border-box; margin: 0; padding: 0; }
  html, body {
    width: 977px; height: 1200px; overflow: hidden;
    background: var(--page-bg);
  }
  .canvas {
    position: relative; width: 977px; height: 1200px;
    font-family: "Source Sans 3", sans-serif; color: var(--ink-body);
  }
  .label {
    position: absolute; left: 91px; width: 795px; height: 252px;
    box-shadow: 0 10px 14px rgba(0,0,0,0.22);
  }
  .label--red { top: 318px; background: var(--label-red-bg); --accent: var(--red); --accent-deep: var(--red-deep); }
  .label--green { top: 630px; background: var(--label-green-bg); --accent: var(--green); --accent-deep: var(--green-deep); }

  /* left column: product information */
  .info { position: absolute; left: 25px; top: 26px; width: 230px; font-size: 8.4px; line-height: 12px; font-weight: 300; white-space: nowrap; }
  .info__title { font-family: "Quicksand", sans-serif; font-weight: 700; font-size: 15px; line-height: 18px; margin-bottom: 18px; color: var(--ink-soft); }
  .info__title .variant { color: var(--accent); }
  .info p { margin-bottom: 9px; }
  .info b { font-weight: 600; color: var(--ink); }

  /* centre: product mark */
  .brand-mark { position: absolute; left: 316px; top: 20px; display: flex; align-items: center; gap: 4px; }
  .brand-mark__dot { width: 10px; height: 10px; border-radius: 50%; background: var(--accent); }
  .brand-mark__name { font-family: "Quicksand", sans-serif; font-weight: 700; font-size: 8px; color: var(--ink); letter-spacing: 0.3px; }
  .hero-art {
    position: absolute; left: 311px; top: 55px; width: 177px; height: 132px; border-radius: 50%;
    background: radial-gradient(ellipse at 55% 50%, var(--accent) 0%, var(--accent-deep) 62%, rgba(0,0,0,0) 72%);
    opacity: 0.85;
  }
  .product-name {
    position: absolute; left: 300px; top: 90px; width: 198px; text-align: center;
    font-family: "Quicksand", sans-serif; font-weight: 700; font-size: 27px; line-height: 29px; color: var(--name-ink);
  }
  .variant-name {
    position: absolute; left: 250px; top: 202px; width: 298px; text-align: center;
    font-family: "Quicksand", sans-serif; font-weight: 700; font-size: 24px; color: var(--ink-soft);
  }
  .label--green .variant-name { font-size: 18px; top: 207px; }

  /* right column: company details */
  .company { position: absolute; right: 27px; top: 26px; width: 210px; text-align: right; font-size: 8.4px; line-height: 12px; font-weight: 300; white-space: nowrap; }
  .company__name { font-family: "Quicksand", sans-serif; font-weight: 700; font-size: 12px; line-height: 14px; color: var(--ink); margin-bottom: 22px; }
  .company p { margin-bottom: 6px; }
  .company b { font-weight: 600; color: var(--ink); }
  .company__web { color: var(--accent); font-weight: 400; font-size: 9px; margin-top: 8px; }
  .company__weight { font-family: "Quicksand", sans-serif; font-weight: 700; font-size: 15px; color: var(--accent); }
</style>
</head>
<body>
<main class="canvas">

  <section class="label label--red" aria-label="Red Chili label">
    <div class="info">
      <h2 class="info__title"><span class="variant">Red Chili</span> Chutney</h2>
      <p><b>Ingredients:</b> Red Pepper (25%), Onion, Pineapple,<br>White Wine Vinegar, Red Chilli (12%), Brown Sugar,<br>Sunflower Oil, Spices, Sugar,<br>Thickener: Starch, Garlic Puree, Ginger Puree, Acidity<br>Regulator: Citric Acid, Salt, Cracked Brown Mustard Seeds.</p>
      <p><b>Allergy Advice:</b> for allergens, see ingredients in bold.<br>Prepared in premises where egg, milk, soya, celery, sulphites<br>and gluten are also used.</p>
      <p><b>Typical values per 100g:</b><br>
        <b>Energy:</b> 343kJ &nbsp;<b>Energy:</b> 80kcal<br>
        <b>Total fat:</b> 2.3g of which saturates: 0.3g<br>
        <b>Carbohydrates:</b> 14g of which <b>Sugars:</b> 12g<br>
        <b>Protein:</b> 1.1g <b>Salt:</b> 0.4g</p>
    </div>
    <div class="brand-mark"><span class="brand-mark__dot"></span><span class="brand-mark__name">BRINDLE FOODS</span></div>
    <div class="hero-art" role="img" aria-label="Illustration of two red chili peppers curving around the product name"></div>
    <div class="product-name">Zintara<br>Chutney</div>
    <div class="variant-name">Red Chili</div>
    <div class="company">
      <div class="company__name">BRINDLE FOODS</div>
      <p>Enjoy with chicken, meat, seafood, salads, sandwiches,<br>potatoes, noodles and rice dishes or simply as a dip!</p>
      <p>For best before end: See lid. Store in a cool dry place.<br>Once opened refrigerate and consume within 4 weeks.</p>
      <p>Produced in the ....... for Address,<br>Address, Address Industrial Estate,<br>Address, Address, <b>Tel:</b> 00000 00000</p>
      <p class="company__web">www.brindlefoods.com</p>
      <div class="company__weight">290g ℮</div>
    </div>
  </section>

  <section class="label label--green" aria-label="Green Chili and Coriander label">
    <div class="info">
      <h2 class="info__title"><span class="variant">Green Chili &amp; Coriander</span></h2>
      <p><b>Ingredients:</b> Red Pepper (25%), Onion, Pineapple,<br>White Wine Vinegar, Red Chilli (12%), Brown Sugar,<br>Sunflower Oil, Spices, Sugar,<br>Thickener: Starch, Garlic Puree, Ginger Puree, Acidity<br>Regulator: Citric Acid, Salt, Cracked Brown Mustard Seeds.</p>
      <p><b>Allergy Advice:</b> for allergens, see ingredients in bold.<br>Prepared in premises where egg, milk, soya, celery, sulphites<br>and gluten are also used.</p>
      <p><b>Typical values per 100g:</b><br>
        <b>Energy:</b> 343kJ &nbsp;<b>Energy:</b> 80kcal<br>
        <b>Total fat:</b> 2.3g of which saturates: 0.3g<br>
        <b>Carbohydrates:</b> 14g of which <b>Sugars:</b> 12g<br>
        <b>Protein:</b> 1.1g <b>Salt:</b> 0.4g</p>
    </div>
    <div class="brand-mark"><span class="brand-mark__dot"></span><span class="brand-mark__name">BRINDLE FOODS</span></div>
    <div class="hero-art" role="img" aria-label="Illustration of two green chili peppers curving around the product name"></div>
    <div class="product-name">Zintara<br>Chutney</div>
    <div class="variant-name">Green Chili &amp; Coriander</div>
    <div class="company">
      <div class="company__name">BRINDLE FOODS</div>
      <p>Enjoy with chicken, meat, seafood, salads, sandwiches,<br>potatoes, noodles and rice dishes or simply as a dip!</p>
      <p>For best before end: See lid. Store in a cool dry place.<br>Once opened refrigerate and consume within 4 weeks.</p>
      <p>Produced in the ....... for Address,<br>Address, Address Industrial Estate,<br>Address, Address, <b>Tel:</b> 00000 00000</p>
      <p class="company__web">www.brindlefoods.com</p>
      <div class="company__weight">290g ℮</div>
    </div>
  </section>

</main>
</body>
</html>
```